VORTRIX ELECTRICAL SOLUTIONS
Stationary Design for Electrical Contractor - Engineering
Stationary Design for Electrical Contractor
Professional
DEAN PULLEN
PO BOX 519 MORANBAH, QLD, 4744
dean@vortrixmail.com.au
Electrical Lic No. 31562
Hi All, Looking for a very modern eye catching stationary design that looks the part.
-Electrical Installs and Maintenance -Split System Installs -Test and Tag -TV and Antenna -Phone and Data -Electrical Fault Finding "Anything Electrical" (please have this in italics)

```html
<!DOCTYPE html>
<html lang="en">
<head>
<meta charset="utf-8">
<title>Vortrix Electrical Solutions – Stationery Set</title>
<link href="https://fonts.googleapis.com/css2?family=Open+Sans:wght@400;700;800&display=swap" rel="stylesheet">
<style>
  :root{
    --orange:#e8501e;
    --charcoal:#2e2e2e;
    --dark:#3b3b3b;
    --grey:#dadada;
    --paper:#ffffff;
    --ink:#444444;
    --muted:#9a9a9a;
  }
  *{box-sizing:border-box;margin:0;padding:0}
  html,body{width:1200px;height:288px;overflow:hidden;background:var(--charcoal);font-family:"Open Sans",Arial,sans-serif}
  .canvas{position:relative;width:1200px;height:288px}
  .zone{position:absolute;top:0;height:288px}
  .zone--stationery{left:0;width:228px;background:var(--charcoal)}
  .zone--folder{left:228px;width:168px;background:var(--grey)}
  .zone--slides{left:396px;width:804px;background:var(--charcoal)}
  .item{position:absolute;background:var(--paper);box-shadow:0 1px 3px rgba(0,0,0,.35);overflow:hidden}
  .item--dark{background:var(--dark)}
  .stripe{position:absolute;left:0;right:0;height:3px;background:var(--orange)}
  .stripe--top{top:0}.stripe--bottom{bottom:0}
  .brand{display:flex;align-items:center;gap:3px;font-weight:800;color:var(--ink);white-space:nowrap;line-height:1}
  .brand__mark{background:var(--orange);flex:none}
  .brand--light{color:var(--paper)}
  .tiny{font-size:3px;color:var(--ink);line-height:1.4;white-space:nowrap}
  .tiny--light{color:#ddd}
  .line{height:1px;background:#ccc;margin:2px 0}
  .slide{position:absolute;width:190px;height:132px;background:var(--paper);overflow:hidden}
  .slide__band{position:absolute;left:0;right:0;bottom:0;height:14px;background:var(--dark)}
  .slide__band::before{content:"";position:absolute;left:0;right:0;top:0;height:3px;background:var(--orange)}
  .slide__head{position:absolute;left:0;right:0;top:0;height:22px;background:var(--dark);border-bottom:3px solid var(--orange);color:var(--paper);font-size:9px;font-weight:700;padding:6px 8px;white-space:nowrap}
  .slide__title{font-size:11px;font-weight:700;color:var(--orange)}
  .slide__center{position:absolute;inset:0 0 14px 0;display:flex;flex-direction:column;align-items:center;justify-content:center;gap:6px}
  .slide__text{position:absolute;left:10px;top:32px;font-size:6px;color:var(--ink);line-height:1.7}
</style>
</head>
<body>
<div class="canvas">

  <section class="zone zone--stationery" aria-label="Printed stationery">
    <div class="item" style="left:8px;top:12px;width:44px;height:26px;padding:4px">
      <div class="brand" style="font-size:4px"><span class="brand__mark" style="width:4px;height:4px"></span>VORTRIX</div>
      <div class="tiny" style="margin-top:5px">Full Name</div>
      <div class="tiny">Job Title</div>
      <div class="stripe stripe--bottom"></div>
    </div>
    <div class="item item--dark" style="left:8px;top:44px;width:44px;height:26px;padding:4px">
      <div class="brand brand--light" style="font-size:4px"><span class="brand__mark" style="width:4px;height:4px"></span>VORTRIX</div>
      <div class="tiny tiny--light" style="margin-top:5px">Your Title</div>
      <div class="stripe stripe--bottom"></div>
    </div>
    <div class="item" style="left:56px;top:12px;width:14px;height:58px">
      <div class="stripe stripe--top"></div>
    </div>
    <div class="item" style="left:76px;top:10px;width:40px;height:56px;padding:4px">
      <div class="brand" style="font-size:4px"><span class="brand__mark" style="width:4px;height:4px"></span>VORTRIX</div>
      <div class="line" style="margin-top:8px"></div><div class="line"></div><div class="line"></div><div class="line"></div><div class="line" style="width:60%"></div>
      <div class="stripe stripe--bottom"></div>
    </div>
    <div class="item" style="left:122px;top:12px;width:62px;height:30px;padding:4px">
      <div class="brand" style="font-size:4px"><span class="brand__mark" style="width:4px;height:4px"></span>VORTRIX</div>
      <div class="tiny" style="margin-top:3px">Street Address Line</div>
      <div class="stripe stripe--bottom"></div>
    </div>
    <div class="item item--dark" style="left:190px;top:12px;width:30px;height:56px">
      <div class="stripe stripe--top"></div>
    </div>
    <div class="item" style="left:122px;top:48px;width:62px;height:20px"><div class="stripe stripe--bottom"></div></div>

    <svg style="position:absolute;left:8px;top:160px" width="36" height="36" viewBox="0 0 36 36" aria-hidden="true">
      <circle cx="18" cy="18" r="17" fill="#fff"/><circle cx="18" cy="18" r="17" fill="none" stroke="var(--orange)" stroke-width="2"/><circle cx="18" cy="18" r="4" fill="var(--charcoal)"/>
    </svg>
    <div class="item" style="left:8px;top:206px;width:36px;height:22px"><div class="stripe stripe--bottom"></div></div>
    <div class="item" style="left:50px;top:160px;width:44px;height:26px;padding:4px">
      <div class="brand" style="font-size:4px"><span class="brand__mark" style="width:4px;height:4px"></span>VORTRIX</div>
      <div class="tiny" style="margin-top:5px">Full Name</div>
      <div class="stripe stripe--bottom"></div>
    </div>
    <div class="item" style="left:50px;top:192px;width:44px;height:26px"><div class="stripe stripe--top"></div></div>
    <div class="item" style="left:100px;top:156px;width:40px;height:56px;padding:4px">
      <div class="brand" style="font-size:4px"><span class="brand__mark" style="width:4px;height:4px"></span>VORTRIX</div>
      <div class="line" style="margin-top:8px"></div><div class="line"></div><div class="line"></div><div class="line" style="width:60%"></div>
      <div class="stripe stripe--bottom"></div>
    </div>
    <div class="item" style="left:146px;top:156px;width:74px;height:34px;padding:4px">
      <div class="brand" style="font-size:5px"><span class="brand__mark" style="width:5px;height:5px"></span>VORTRIX</div>
      <div class="stripe stripe--bottom"></div>
    </div>
    <div class="item" style="left:146px;top:196px;width:74px;height:34px"><div class="stripe stripe--top"></div></div>
  </section>

  <section class="zone zone--folder" aria-label="Presentation folder">
    <div class="item" style="left:10px;top:14px;width:74px;height:110px;padding:6px">
      <div class="line" style="margin-top:50px"></div><div class="line"></div>
    </div>
    <div class="item" style="left:84px;top:14px;width:74px;height:110px;display:flex;align-items:center;justify-content:center">
      <div class="brand" style="font-size:9px"><span class="brand__mark" style="width:9px;height:9px"></span>VORTRIX</div>
      <div class="stripe stripe--bottom"></div>
    </div>
    <div class="item" style="left:10px;top:150px;width:74px;height:110px"><div class="stripe stripe--bottom"></div></div>
    <div class="item" style="left:84px;top:150px;width:74px;height:110px;display:flex;align-items:center;justify-content:center">
      <div class="brand" style="font-size:8px"><span class="brand__mark" style="width:8px;height:8px"></span>VORTRIX</div>
      <div class="stripe stripe--bottom"></div>
    </div>
  </section>

  <section class="zone zone--slides" aria-label="Presentation slides">
    <article class="slide" style="left:8px;top:10px">
      <div class="slide__center">
        <div class="brand" style="font-size:16px"><span class="brand__mark" style="width:16px;height:16px"></span>VORTRIX</div>
        <div style="font-size:7px;font-weight:700;color:var(--ink);letter-spacing:1px">WELCOME</div>
      </div>
      <div class="slide__band"></div>
    </article>
    <article class="slide" style="left:207px;top:10px">
      <div style="position:absolute;left:10px;top:14px">
        <div class="slide__title">Presentation Title</div>
        <div style="font-size:6px;font-weight:700;color:var(--ink)">1999-2015</div>
      </div>
      <div class="brand" style="position:absolute;left:10px;top:74px;font-size:12px"><span class="brand__mark" style="width:12px;height:12px"></span>VORTRIX</div>
      <div class="slide__band"></div>
    </article>
    <article class="slide" style="left:406px;top:10px">
      <div class="slide__head">Sub Title Lorem Ipsum</div>
      <svg style="position:absolute;left:40px;top:36px" width="110" height="70" viewBox="0 0 110 70" aria-label="Bar chart">
        <line x1="0" y1="69" x2="110" y2="69" stroke="#bbb"/>
        <rect x="8" y="44" width="16" height="25" fill="#9a9a9a"/>
        <rect x="32" y="32" width="16" height="37" fill="#6f6f6f"/>
        <rect x="56" y="20" width="16" height="49" fill="var(--dark)"/>
        <rect x="80" y="4" width="16" height="65" fill="var(--orange)"/>
      </svg>
      <div class="slide__band"></div>
    </article>
    <article class="slide" style="left:605px;top:10px">
      <div class="slide__head">Sub Title Lorem Ipsum</div>
      <div class="slide__text">• Lorem ipsum dolor sit<br>• Amet consectetur elit<br>• Sed do eiusmod<br>• Tempor incididunt ut</div>
      <div class="slide__band"></div>
    </article>

    <article class="slide" style="left:8px;top:150px">
      <div class="slide__center">
        <div class="brand" style="font-size:14px"><span class="brand__mark" style="width:14px;height:14px"></span>VORTRIX</div>
      </div>
      <div class="slide__band"></div>
    </article>
    <article class="slide" style="left:207px;top:150px">
      <div class="slide__head">Sub Title Lorem Ipsum</div>
      <div class="slide__text">Lorem ipsum dolor sit amet.</div>
      <div style="position:absolute;left:10px;top:52px;width:80px;height:50px;background:var(--grey)" role="img" aria-label="Photo of electrical work"></div>
      <div class="slide__band"></div>
    </article>
    <article class="slide" style="left:406px;top:150px">
      <div class="slide__head">Sub Title Lorem Ipsum</div>
      <svg style="position:absolute;left:62px;top:32px" width="70" height="70" viewBox="-35 -35 70 70" aria-label="Pie chart">
        <circle r="32" fill="var(--orange)"/>
        <path d="M0 0 L0 -32 A32 32 0 0 1 30.4 9.9 Z" fill="var(--dark)"/>
        <path d="M0 0 L30.4 9.9 A32 32 0 0 1 -9.9 30.4 Z" fill="#9a9a9a"/>
      </svg>
      <div class="slide__band"></div>
    </article>
    <article class="slide" style="left:605px;top:150px">
      <div class="slide__center">
        <div style="font-size:18px;font-weight:700;color:var(--orange)">Thank You</div>
        <div class="brand" style="font-size:10px"><span class="brand__mark" style="width:10px;height:10px"></span>VORTRIX</div>
      </div>
      <div class="slide__band"></div>
    </article>
  </section>
</div>
</body>
</html>
```